Breezeway Masters Business Card Design

Design new, 2 sides, business cards for a residential and light commercial heating, air conditioning contractor.

Target Market(s)

Homeowners, small businesses

Industry/Entity Type

Business

Contact Information for Business Card

Dominic Halvorsen
Phone - 862-415-2763
Email
Address - PO box 648
Succasunna NJ 07876
Website - www.BreezewayMastersLLC.example

Requirements
Must have
• logo, company colors, standard size with no die cut, so I can use nimbo press

```html
<!DOCTYPE html>
<html lang="en">
<head>
<meta charset="utf-8">
<title>Breezeway Masters Business Card</title>
<link href="https://fonts.googleapis.com/css2?family=Montserrat:wght@400;600;700&display=swap" rel="stylesheet">
<style>
  :root {
    --stage: #d1d2d4;
    --card-light: #ffffff;
    --card-dark: #211f20;
    --brand-red: #9b1f2e;
    --brand-orange: #f58a2c;
    --ink: #1e1e1e;
    --ink-light: #f2f2f2;
  }
  html, body {
    margin: 0;
    padding: 0;
    width: 1200px;
    height: 927px;
    overflow: hidden;
    background: var(--stage);
    font-family: "Montserrat", sans-serif;
  }
  .canvas {
    position: relative;
    width: 1200px;
    height: 927px;
  }
  .card {
    position: absolute;
    top: 95px;
    width: 421px;
    height: 737px;
    border-radius: 36px;
    text-align: center;
  }
  .card--front { left: 155px; background: var(--card-light); color: var(--ink); }
  .card--back  { left: 623px; background: var(--card-dark); color: var(--ink-light); }

  .brand-name {
    position: absolute;
    left: 0;
    right: 0;
    margin: 0;
    font-weight: 700;
    font-size: 44px;
    line-height: 1.05;
    letter-spacing: 1px;
  }
  .card--front .brand-name { top: 108px; color: var(--brand-red); }
  .card--back .brand-name  { top: 323px; color: var(--brand-orange); }

  .contact {
    position: absolute;
    left: 0;
    right: 0;
    top: 445px;
  }
  .contact__name {
    margin: 0;
    font-size: 29px;
    font-weight: 600;
    color: var(--brand-orange);
    letter-spacing: 0.5px;
    line-height: 1.2;
  }
  .contact__role {
    margin: 2px 0 0;
    font-size: 18px;
    line-height: 1.2;
  }
  .contact__address {
    margin: 14px 0 0;
    font-size: 18.5px;
    line-height: 23px;
    font-style: normal;
  }
  .contact__icons {
    display: flex;
    justify-content: center;
    gap: 5px;
    margin-top: 16px;
  }
  .contact__icons svg { width: 14px; height: 14px; }
  .contact__lines {
    margin: 14px 0 0;
    font-size: 18.5px;
    line-height: 23px;
  }
  .contact__lines p { margin: 0; }
  .highlight { color: var(--brand-orange); }

  .card--back .web {
    position: absolute;
    left: 0;
    right: 0;
    bottom: 40px;
    margin: 0;
    font-size: 18.5px;
  }
</style>
</head>
<body>
<div class="canvas">

  <section class="card card--front">
    <h1 class="brand-name">BREEZEWAY<br>MASTERS</h1>

    <div class="contact">
      <p class="contact__name">DOMINIC HALVORSEN</p>
      <p class="contact__role">Director</p>
      <address class="contact__address">P.O. Box 648<br>Succasunna, NJ 07876</address>

      <div class="contact__icons" aria-hidden="true">
        <svg viewBox="0 0 16 16" fill="none" stroke="#f58a2c" stroke-width="1.4" stroke-linecap="round" stroke-linejoin="round">
          <path d="M4 2 L6 5 L5 7 Q7 10 9 11 L11 10 L14 12 L12 14 Q6 14 2 4 Z"/>
        </svg>
        <svg viewBox="0 0 16 16" fill="none" stroke="#f58a2c" stroke-width="1.4">
          <rect x="4.5" y="1.5" width="7" height="13" rx="1"/>
          <line x1="7" y1="12.3" x2="9" y2="12.3"/>
        </svg>
        <svg viewBox="0 0 16 16" fill="none" stroke="#f58a2c" stroke-width="1.4" stroke-linejoin="round">
          <rect x="1.5" y="3.5" width="13" height="9"/>
          <path d="M1.5 3.5 L8 9 L14.5 3.5"/>
        </svg>
        <svg viewBox="0 0 16 16" fill="none" stroke="#f58a2c" stroke-width="1.2">
          <circle cx="8" cy="8" r="6.5"/>
          <ellipse cx="8" cy="8" rx="3" ry="6.5"/>
          <line x1="1.5" y1="8" x2="14.5" y2="8"/>
          <line x1="2.5" y1="5" x2="13.5" y2="5"/>
          <line x1="2.5" y1="11" x2="13.5" y2="11"/>
        </svg>
      </div>

      <div class="contact__lines">
        <p>862-415-2763</p>
        <p>862-415-2790</p>
        <p>info@breezewaymasters.example</p>
        <p>www.<span class="highlight">breezewaymasters</span>.example</p>
      </div>
    </div>
  </section>

  <section class="card card--back">
    <h2 class="brand-name">BREEZEWAY<br>MASTERS</h2>
    <p class="web">www.<span class="highlight">breezewaymasters</span>.example</p>
  </section>

</div>
</body>
</html>
```